Brochure Design Project

We are a manufacturing business based in Archerfield, Australia. We service the air conditioning industry. Our brochure will have some of our information and history on one side, followed by a list of products and services on the back.

Our current logo must be used.

Size will be

216mm x 279mm

Double sided.

Target Market(s)

air conditioning contractors

Industry/Entity Type

Air Conditioning

Requirements
Must have
• Must haves

Company history paragraph

Corvel Insulation Has been established in the HVAC industry since 1984. It has grown from 2 to 16 employees.

We pride ourselves on offering the fastest lagging service in Brisbane. With our new CNC machine we can meet any demands large or small.

services-
Internal and external insulating of HVAC ductwork
Manufacture of metal cushion boxes
Manufacture of ductboard cushion boxes
Cut and facing of insulation to size and shape.

Products-
glasswool insulation
ductboard
Closed cell foam
Sonthex
Ceramic board
variety of foils
metal spigots
pins and clips

Pictures of our products

Factory location-
47 Merrilong Street
Archerfield, QLD, 4152

Telephone number-
07 3190 4623

Email address-
ray@corvelinsulation.example.com.au

```html
<!DOCTYPE html>
<html lang="en">
<head>
<meta charset="utf-8">
<title>Corvel Insulation – Products</title>
<link href="https://fonts.googleapis.com/css2?family=PT+Sans:wght@400;700&display=swap" rel="stylesheet">
<style>
  :root {
    --ink: #1c1c1c;
    --paper: #ffffff;
    --peach-top: #fdf1e8;
    --peach-mid: #fac39a;
    --orange: #f28a3a;
    --orange-deep: #ef7d22;
    --frame: #1a1a1a;
    --label: #ffffff;
  }
  html, body {
    margin: 0;
    padding: 0;
    width: 939px;
    height: 1200px;
    overflow: hidden;
    background: var(--paper);
    font-family: "PT Sans", Arial, sans-serif;
  }
  .sheet {
    position: absolute;
    left: 22px;
    top: 21px;
    width: 894px;
    height: 1157px;
    border: 2px solid var(--frame);
    box-shadow: 3px 4px 4px rgba(0,0,0,0.35);
    overflow: hidden;
    background: linear-gradient(180deg, var(--peach-top) 0%, #fde0c9 25%, var(--peach-mid) 50%, #f6a262 72%, var(--orange) 88%);
  }
  .backdrop {
    position: absolute;
    left: 0;
    top: 0;
    width: 894px;
    height: 1157px;
  }
  .ornament-area {
    position: absolute;
    left: 470px;
    top: 570px;
    width: 424px;
    height: 587px;
    background: radial-gradient(ellipse at 60% 45%, rgba(255,255,255,0.35) 0%, rgba(255,255,255,0.12) 45%, rgba(255,255,255,0) 70%);
  }
  .section-title {
    position: absolute;
    left: 51px;
    top: 83px;
    margin: 0;
    font-size: 21px;
    font-weight: 700;
    letter-spacing: 0.2px;
    color: var(--ink);
  }
  .product-photo {
    position: absolute;
    width: 242px;
    height: 139px;
  }
  .product-photo .label {
    position: absolute;
    color: var(--label);
    font-size: 15.5px;
    line-height: 1.05;
    white-space: nowrap;
    text-shadow: 0 0 3px rgba(0,0,0,0.45);
  }
  .product-photo .label.dark { color: var(--ink); text-shadow: none; }
  .foam { left: 51px; top: 141px; background: linear-gradient(180deg, #6f7071 0%, #4e5051 100%); }
  .glass-stack { left: 320px; top: 141px; background: linear-gradient(180deg, #ece01f 0%, #d9c61a 100%); }
  .glass-slab { left: 587px; top: 141px; background: linear-gradient(180deg, #f0ead4 0%, #e9cd6a 60%, #f3efe4 100%); }
  .duct-sheet { left: 51px; top: 301px; background: linear-gradient(180deg, #555556 0%, #404041 100%); }
  .duct-spigots { left: 320px; top: 301px; background: linear-gradient(180deg, #cfd1d4 0%, #aeb1b4 100%); }
  .pins { left: 587px; top: 302px; background: linear-gradient(180deg, #8d8fa6 0%, #7e819c 100%); }
  .foils { left: 51px; top: 468px; background: linear-gradient(180deg, #7c7d7f 0%, #525355 100%); }
  .spigot { left: 320px; top: 465px; width: 240px; height: 135px; background: linear-gradient(180deg, #dfeaf4 0%, #9fbcd4 100%); }
  .product-list {
    position: absolute;
    left: 51px;
    top: 644px;
    margin: 0;
    padding: 0;
    list-style: none;
  }
  .product-list li {
    position: relative;
    padding-left: 33px;
    font-size: 22px;
    line-height: 28.2px;
    color: var(--ink);
  }
  .product-list li::before {
    content: "";
    position: absolute;
    left: 6px;
    top: 9px;
    width: 8px;
    height: 8px;
    border: 1.5px solid var(--ink);
    background: var(--paper);
    transform: rotate(45deg);
  }
  .brand {
    position: absolute;
    left: 52px;
    top: 1068px;
    display: flex;
    align-items: center;
    gap: 10px;
  }
  .brand-mark {
    width: 20px;
    height: 20px;
    background: var(--orange-deep);
  }
  .brand-name {
    font-size: 20px;
    font-weight: 700;
    color: #3a3a3a;
  }
</style>
</head>
<body>
  <main class="sheet">
    <svg class="backdrop" viewBox="0 0 894 1157" aria-hidden="true">
      <path d="M0,1022 C300,960 640,880 894,790 L894,1157 L0,1157 Z" fill="#1a1a1a" />
      <path d="M0,1032 C300,970 640,892 894,802 L894,1157 L0,1157 Z" fill="#f07f26" />
      <path d="M0,1048 C320,990 650,905 894,830 L894,1157 L0,1157 Z" fill="#ffffff" />
    </svg>

    <div class="ornament-area" role="img" aria-label="Decorative overlapping outlined squares in white and orange"></div>

    <h1 class="section-title">PRODUCTS</h1>

    <div class="product-photo foam" role="img" aria-label="Photo of a closed cell foam sheet with peel-off backing"><span class="label" style="right:10px;bottom:10px;">Closed Cell Foam</span></div>
    <div class="product-photo glass-stack" role="img" aria-label="Photo of stacked yellow glasswool insulation sheets"><span class="label dark" style="left:11px;top:12px;">Glasswool Insulation</span></div>
    <div class="product-photo glass-slab" role="img" aria-label="Photo of a glasswool insulation slab"><span class="label dark" style="left:16px;top:12px;">Glasswool Insulation</span></div>

    <div class="product-photo duct-sheet" role="img" aria-label="Photo of a dark ductboard panel"><span class="label" style="left:11px;top:8px;">Ductboard</span></div>
    <div class="product-photo duct-spigots" role="img" aria-label="Photo of ductboard boxes fitted with round spigots"><span class="label" style="right:17px;top:13px;">Ductboard</span></div>
    <div class="product-photo pins" role="img" aria-label="Photo of insulation pins and clips"><span class="label" style="right:10px;top:11px;">Pins and Clips</span></div>

    <div class="product-photo foils" role="img" aria-label="Photo of perforated foil sheet"><span class="label" style="left:11px;top:14px;">Variety of Foils</span></div>
    <div class="product-photo spigot" role="img" aria-label="Photo of a metal spigot"><span class="label dark" style="right:16px;bottom:12px;text-align:center;">Metal<br>Spigots</span></div>

    <ul class="product-list">
      <li>Ceramic Board</li>
      <li>Closed Cell Foam</li>
      <li>Ductboard</li>
      <li>Glasswool Insulation</li>
      <li>Metal Spigots</li>
      <li>Pins and Clips</li>
      <li>Sonthex</li>
      <li>Variety of Foils</li>
    </ul>

    <div class="brand">
      <span class="brand-mark"></span>
      <span class="brand-name">Corvel Insulation</span>
    </div>
  </main>
</body>
</html>
```